Business Identity Stationary

Already have the logo which is in the attached files so only need the Business STationary
1) Double Sided Business Card
2) Letterhead
3) Presentation folder with business card holder on inside cover
4) WIth compliments slip
See information for business cards, letterhead and presentation folder below.
http://files.pixelbazaar-example.com/img/771204/40612/40612_3918825_771204_thumb.jpg
Updates

This should be a simply job using a logo we already had designed along with a little device. I suggest using the device off center and perhaps lower in the corner in an abstract way. Also the logo device could be used as a watermark for the letterhead. The designer who created the logo presented something that I think works well for a business card. The front of the double sided business card could have the name logo small for the website address and only use the Lime device on the front. Then on the back could be the name Brevar Consulting logo.

Please note that for the business card the black and lime green background do look good. Also please think of using the lime device separately in an unusual way.

It has been brought to my attention that.my budget was far to low. Hopefully this.will attract you to the project. 

The parent company of Brevar Consulting is TallHeron investments. I have uploaded a file of the Tall Heron business card I really like. Perhaps use this business card as a guide to the type of modern and clean style I am looking for. It also works to have the Brevar Consultign and Tall Heron similar.

Reason: Still haven't received anything exactly right.

Industry/Entity Type

Business

Font styles to use
Sans Serif

Colors
9bcb3c
000000
5c5c5c
add136
cadf82
eaf2cf
f9fbf2
1b1b1b
757575

Requirements
Must have
• 1) Double Sided Business Card
Marta Delvorin
Director
Tel: +505 8290 3357
Email: mkd@brevarconsulting-example.com
Website: www.brevarconsulting-example.com

Everett Delvorin
Director
Tel: +505 8290 3362
Email: ekd@brevarconsulting-example.com

Lucia Pardo Ventrosa
Director
Tel: 8442 6183
Email: lpv@brevarconsulting-example.com

2) Letterhead
Logo
Lime Logo Device
Website Address: www.brevarconsulting-example.com
Small print on bottom: Brevar Consulting a Tall Heron Investment Company SA. RUC K0720000483915

3) Presentation Folder
Traditional Presentation folder with inside front cover spot for the insertion of business card.

4) With Compliments slip

```html
<!DOCTYPE html>
<html lang="en">
<head>
<meta charset="utf-8">
<title>Brevar Consulting — Letterhead</title>
<link href="https://fonts.googleapis.com/css2?family=Montserrat:wght@300;400;500&display=swap" rel="stylesheet">
<style>
  :root {
    --lime: #8dc63f;
    --lime-soft: #9bcb3c;
    --ink: #1b1b1b;
    --ink-mid: #5c5c5c;
    --mark-faint: #dcdcdc;
    --paper: #ffffff;
  }
  * { margin: 0; padding: 0; box-sizing: border-box; }
  html, body { width: 848px; height: 1200px; overflow: hidden; background: var(--paper); }
  .letterhead {
    position: relative;
    width: 848px;
    height: 1200px;
    background: var(--paper);
    font-family: "Montserrat", sans-serif;
    color: var(--ink);
  }
  .brand-name {
    position: absolute;
    left: 28px;
    top: 22px;
    color: var(--ink-mid);
    font-weight: 300;
    line-height: 1;
  }
  .brand-name .line-main { display: block; font-size: 44px; letter-spacing: -1px; }
  .brand-name .line-sub { display: block; font-size: 17px; letter-spacing: 7px; margin-top: 6px; }

  .watermark {
    position: absolute;
    left: 0;
    top: 440px;
    width: 848px;
    text-align: center;
    color: var(--mark-faint);
    font-weight: 300;
    line-height: 1;
  }
  .watermark .line-main { display: block; font-size: 150px; letter-spacing: -4px; }
  .watermark .line-sub { display: block; font-size: 56px; letter-spacing: 38px; margin-top: 18px; padding-left: 38px; }

  .footer-band {
    position: absolute;
    left: 0;
    top: 1078px;
    width: 610px;
    height: 79px;
    background: var(--lime);
  }
  .footer-web {
    position: absolute;
    left: 64px;
    top: 7px;
    font-size: 21px;
    font-weight: 500;
    letter-spacing: 1px;
    color: var(--ink);
  }
  .footer-company {
    position: absolute;
    left: 64px;
    top: 36px;
    font-size: 12.5px;
    font-weight: 400;
    color: var(--ink);
    white-space: nowrap;
  }
  .footer-ruc {
    position: absolute;
    left: 216px;
    top: 56px;
    font-size: 11px;
    font-weight: 400;
    color: var(--ink);
  }
  .footer-bar {
    position: absolute;
    top: 1078px;
    height: 79px;
    background: var(--lime);
  }
  .footer-bar.one { left: 618px; width: 20px; }
  .footer-bar.two { left: 647px; width: 34px; }
  .footer-bar.three { left: 690px; width: 22px; }
  .footer-dot {
    position: absolute;
    left: 746px;
    top: 1088px;
    width: 72px;
    height: 72px;
    border-radius: 50%;
    background: var(--lime-soft);
  }
</style>
</head>
<body>
  <main class="letterhead">
    <div class="brand-name">
      <span class="line-main">BREVAR</span>
      <span class="line-sub">consulting</span>
    </div>

    <div class="watermark" aria-hidden="true">
      <span class="line-main">BREVAR</span>
      <span class="line-sub">consulting</span>
    </div>

    <footer>
      <div class="footer-band">
        <p class="footer-web">WWW.BREVARCONSULTING-EXAMPLE.COM</p>
        <p class="footer-company">BREVAR CONSULTING A TALL HERON INVESTMENT COMPANY SA</p>
        <p class="footer-ruc">RUC K0720000483915</p>
      </div>
      <div class="footer-bar one"></div>
      <div class="footer-bar two"></div>
      <div class="footer-bar three"></div>
      <div class="footer-dot"></div>
    </footer>
  </main>
</body>
</html>
```